Korimet Business Cards

Korimet is a software startup and we are looking for business cards that help convey our employee personalities, as well as the professionalism of the company.
Our company font is Comfortaa - and the company logo is attached (we are okay having the text beside the logo if applicable) where we can find the company colour scheme. Cards can be horizontal or vertical format.
We are looking for a two sided business card - on the front we will see the personal details of the employee (name, position, email and phone number), and then on the back, we will see the business details (name and logo, address, phone number, website, email, company tagline: "Driving Smarter Software for the Next Generation of Vehicles")
We want the design to be clean and simple, but also fun, modern, and capturing of a young startup vibe.

```html
<!DOCTYPE html>
<html lang="en">
<head>
<meta charset="utf-8">
<title>Korimet Business Cards</title>
<link href="https://fonts.googleapis.com/css2?family=Comfortaa:wght@400;600;700&display=swap" rel="stylesheet">
<style>
  :root {
    --page: #c9cbcc;
    --card: #0e0f22;
    --band: #5a4fab;
    --brand: #5d51b3;
    --accent: #ea5d6c;
    --text: #ffffff;
    --sphere-violet: #6b4a9a;
    --sphere-slate: #3a3b4a;
  }
  * { box-sizing: border-box; margin: 0; padding: 0; }
  html, body { width: 1200px; height: 928px; overflow: hidden; }
  body {
    background: var(--page);
    font-family: "Comfortaa", sans-serif;
    color: var(--text);
    position: relative;
  }
  .card {
    position: absolute;
    background: var(--card);
    border-radius: 16px;
    overflow: hidden;
  }
  .card--back { left: 267px; top: 59px; width: 669px; height: 383px; }
  .card--front { left: 264px; top: 484px; width: 676px; height: 387px; }
  .spheres { position: absolute; inset: 0; width: 100%; height: 100%; }

  .brand { position: absolute; display: flex; flex-direction: column; align-items: center; }
  .brand__dot { border-radius: 50%; background: var(--brand); }
  .brand__name { font-weight: 700; color: var(--brand); letter-spacing: 1px; line-height: 1; }

  .card--back .brand { left: 0; right: 0; top: 54px; }
  .card--back .brand__dot { width: 96px; height: 96px; margin-bottom: 24px; }
  .card--back .brand__name { font-size: 46px; }

  .tagline {
    position: absolute; left: 0; right: 0; top: 257px;
    text-align: center; font-size: 16.5px; letter-spacing: 0.3px;
  }
  .contact-band {
    position: absolute; left: 0; right: 0; top: 284px; bottom: 0;
    background: var(--band);
    border-top: 3px solid var(--accent);
  }
  .contact-band__row {
    position: absolute; left: 0; right: 0;
    display: flex; justify-content: center; gap: 28px;
    font-size: 16.5px; letter-spacing: 0.8px;
  }
  .contact-band__row--top { top: 15px; }
  .contact-band__row--bottom { top: 44px; }

  .contact { display: flex; align-items: center; gap: 6px; white-space: nowrap; }
  .icon { width: 16px; height: 16px; flex: none; }

  .card--front .brand { left: 128px; width: 200px; top: 118px; }
  .card--front .brand__dot { width: 88px; height: 88px; margin-bottom: 18px; }
  .card--front .brand__name { font-size: 42px; }

  .divider { position: absolute; left: 336px; }
  .divider--red-top { top: 116px; height: 32px; background: var(--accent); width: 2px; }
  .divider--purple { top: 151px; height: 82px; background: var(--brand); width: 5px; left: 335px; }
  .divider--red-bottom { top: 236px; height: 34px; background: var(--accent); width: 2px; }

  .person { position: absolute; left: 365px; top: 116px; }
  .person__name { color: var(--accent); font-size: 28px; font-weight: 700; letter-spacing: 1px; }
  .person__role { font-size: 17px; margin-top: 6px; letter-spacing: 0.5px; }
  .person__contacts { list-style: none; margin-top: 22px; font-size: 17px; letter-spacing: 0.8px; }
  .person__contacts li { margin-bottom: 11px; }
</style>
</head>
<body>

<section class="card card--back" aria-label="Company side">
  <svg class="spheres" viewBox="0 0 669 383" aria-hidden="true">
    <defs>
      <radialGradient id="violet" cx="30%" cy="25%" r="80%">
        <stop offset="0" stop-color="var(--sphere-violet)"/><stop offset="1" stop-color="var(--card)"/>
      </radialGradient>
      <radialGradient id="slate" cx="70%" cy="30%" r="80%">
        <stop offset="0" stop-color="var(--sphere-slate)"/><stop offset="1" stop-color="var(--card)"/>
      </radialGradient>
    </defs>
    <circle cx="45" cy="41" r="20" fill="url(#violet)"/>
    <circle cx="590" cy="74" r="51" fill="url(#violet)"/>
    <circle cx="76" cy="191" r="50" fill="url(#slate)"/>
    <circle cx="621" cy="224" r="22" fill="url(#slate)"/>
  </svg>

  <div class="brand">
    <span class="brand__dot"></span>
    <span class="brand__name">korimet</span>
  </div>

  <p class="tagline">Driving Smarter Software for the Next Generation of Vehicles</p>

  <div class="contact-band">
    <div class="contact-band__row contact-band__row--top">
      <span class="contact">
        <svg class="icon" viewBox="0 0 16 16"><circle cx="8" cy="8" r="8" fill="var(--accent)"/><path d="M5 4.5l1.5-.5 1 2-1 .8a5 5 0 0 0 2.7 2.7l.8-1 2 1-.5 1.5c-3 .5-7-3.5-6.5-6.5z" fill="#fff"/></svg>
        1-844-555-0147</span>
      <span class="contact">
        <svg class="icon" viewBox="0 0 16 16"><circle cx="8" cy="8" r="8" fill="var(--accent)"/><rect x="4" y="5.5" width="8" height="5.5" rx="0.8" fill="#fff"/><path d="M4.3 5.8L8 8.6l3.7-2.8" stroke="var(--accent)" stroke-width="0.9" fill="none"/></svg>
        info@korimet.ai</span>
      <span class="contact">
        <svg class="icon" viewBox="0 0 16 16"><circle cx="8" cy="8" r="8" fill="var(--accent)"/><circle cx="8" cy="8" r="4.5" fill="none" stroke="#fff" stroke-width="1.2"/><path d="M3.5 8h9M8 3.5c-2 2.5-2 6.5 0 9M8 3.5c2 2.5 2 6.5 0 9" stroke="#fff" stroke-width="0.9" fill="none"/></svg>
        www.korimet.ai</span>
    </div>
    <div class="contact-band__row contact-band__row--bottom">
      <span class="contact">
        <svg class="icon" viewBox="0 0 16 16"><path d="M8 1a5 5 0 0 1 5 5c0 4-5 9-5 9S3 10 3 6a5 5 0 0 1 5-5z" fill="var(--accent)"/><circle cx="8" cy="6" r="2" fill="var(--band)"/></svg>
        Suite 210, 880 Maple Ave W, Riverton, ON K7L 4B2</span>
    </div>
  </div>
</section>

<section class="card card--front" aria-label="Personal side">
  <svg class="spheres" viewBox="0 0 676 387" aria-hidden="true">
    <defs>
      <radialGradient id="violet2" cx="30%" cy="25%" r="80%">
        <stop offset="0" stop-color="var(--sphere-violet)"/><stop offset="1" stop-color="var(--card)"/>
      </radialGradient>
      <radialGradient id="slate2" cx="70%" cy="30%" r="80%">
        <stop offset="0" stop-color="var(--sphere-slate)"/><stop offset="1" stop-color="var(--card)"/>
      </radialGradient>
    </defs>
    <circle cx="44" cy="98" r="20" fill="url(#violet2)"/>
    <circle cx="594" cy="131" r="51" fill="url(#violet2)"/>
    <circle cx="77" cy="249" r="50" fill="url(#slate2)"/>
    <circle cx="627" cy="284" r="21" fill="url(#slate2)"/>
  </svg>

  <div class="brand">
    <span class="brand__dot"></span>
    <span class="brand__name">korimet</span>
  </div>

  <span class="divider divider--red-top"></span>
  <span class="divider divider--purple"></span>
  <span class="divider divider--red-bottom"></span>

  <div class="person">
    <h1 class="person__name">Maya Torres</h1>
    <p class="person__role">Director</p>
    <ul class="person__contacts">
      <li class="contact">
        <svg class="icon" viewBox="0 0 16 16"><circle cx="8" cy="8" r="8" fill="var(--accent)"/><path d="M5 4.5l1.5-.5 1 2-1 .8a5 5 0 0 0 2.7 2.7l.8-1 2 1-.5 1.5c-3 .5-7-3.5-6.5-6.5z" fill="#fff"/></svg>
        1-844-555-0147</li>
      <li class="contact">
        <svg class="icon" viewBox="0 0 16 16"><circle cx="8" cy="8" r="8" fill="var(--accent)"/><rect x="4" y="5.5" width="8" height="5.5" rx="0.8" fill="#fff"/><path d="M4.3 5.8L8 8.6l3.7-2.8" stroke="var(--accent)" stroke-width="0.9" fill="none"/></svg>
        info@korimet.ai</li>
      <li class="contact">
        <svg class="icon" viewBox="0 0 16 16"><circle cx="8" cy="8" r="8" fill="var(--accent)"/><circle cx="8" cy="8" r="4.5" fill="none" stroke="#fff" stroke-width="1.2"/><path d="M3.5 8h9M8 3.5c-2 2.5-2 6.5 0 9M8 3.5c2 2.5 2 6.5 0 9" stroke="#fff" stroke-width="0.9" fill="none"/></svg>
        www.korimet.ai</li>
    </ul>
  </div>
</section>

</body>
</html>
```